Attractive WP design (Astra) for our textile production and trading business

We need a design for our new website. We would like it to be based on the WP theme Astra.

1) Description of the business
Kelvaro GmbH is a textile company that is specialized in production and trading of high-quality cotton fabrics/products.

We…
• design and develop
• weave (incl. special weaving/embroidery technique)
• shear
• finish the products (Logo printing, packing)

Our products are…
• Swiss Ghutra
• Shemagh (=Yashmagh) (https://www.vontrema.ch/en/competence/clothing-textiles/clothing-for-arab-and-african-markets/#210)
• Desdasha’s (https://www.vontrema.ch/en/competence/clothing-textiles/clothing-for-arab-and-african-markets/#210)
• Emmas and Shawls
Emmas are traditional head coverings worn by Muslim man in Sudan. The cloth of exactly 5 yards in length is winded around the head like a turban. The cloth can be plain white, have a decorative trim or be colored. There are also matching scarfs.
• Brocade/Damask
• Atiku
• Teminor Voile (https://plovadesk.com/products/teminor-3?_pos=2&_sid=98a067e86&_ss=r)
--> Please see attached pictures of the different fabrics and products

2) Target audience and users
• (Foreign) wholesalers interested in trading with Kelvaro

3) Goals of the website
Kelvaro has been a family-run textile business for 17 years with no web presence. The majority of our historical sales have been based on pre-existing relationships or word-of-mouth connections. Now, we seek to diversify our customer base. For this, we want our first website/online presence in order to:

• Enable foreign wholesalers to discover Kelvaro as a supplier of Swiss quality fabric;
• Showcase both our current specific product line as well as our general manufacturing capabilities for new custom products;
• Enable inquiries/orders by interested parties

4) Design wishes
The design should reflect our high quality textiles. The design should be clean, inviting, friendly and professional. Colors can be chosen freely. Pictures should not overload sites but support our goal to attract and inspire future buyers.

If you have any questions, please reach out to us!

• the site will be multilingual (german/english/possibly french)

```html
<!DOCTYPE html>
<html lang="en">
<head>
<meta charset="utf-8">
<title>Kelvaro – Cotton Fabrics</title>
<link href="https://fonts.googleapis.com/css2?family=Montserrat:wght@400;500;600;700&family=Lato:ital,wght@0,400;0,700;1,400&display=swap" rel="stylesheet">
<style>
:root{
  --orange:#e98c41;
  --dark:#1f1f1f;
  --footer:#262626;
  --text:#555;
  --light:#f5f5f5;
  --white:#fff;
}
*{box-sizing:border-box;margin:0;padding:0}
html,body{width:1200px;height:4418px;overflow:hidden}
body{position:relative;background:var(--white);font-family:'Lato',sans-serif;color:var(--text)}
.abs{position:absolute}
.head-font{font-family:'Montserrat',sans-serif}

/* header */
.site-logo{left:111px;top:30px;display:flex;align-items:center;gap:12px;font-family:'Montserrat',sans-serif;font-weight:700;font-size:34px;color:var(--dark)}
.site-logo .dot{width:26px;height:26px;border-radius:50%;background:var(--dark)}
.topbar{right:112px;top:20px;font-size:17px;color:#222;display:flex;gap:10px;align-items:center}
.topbar svg{vertical-align:-2px}
.topbar .lang{margin-left:18px}
.main-nav{top:68px;left:485px;font-family:'Montserrat',sans-serif;font-weight:500;font-size:17px;color:#222}
.main-nav span{position:absolute;white-space:nowrap}
.main-nav .active{color:var(--orange)}

/* hero */
.hero{left:0;top:112px;width:1200px;height:556px;background:linear-gradient(100deg,#8a847c 0%,#b8b0a4 30%,#7d8a96 48%,#c9bca9 60%,#8a2b4d 75%,#5d1f3c 88%,#3c3f63 100%)}
.hero-title{left:108px;top:236px;font-family:'Montserrat',sans-serif;font-weight:600;font-size:66px;color:var(--white);letter-spacing:1px}
.hero-sub{left:112px;top:322px;font-size:20px;line-height:32px;color:var(--white)}
.btn-light{left:111px;top:415px;width:186px;height:65px;background:var(--white);color:#111;font-family:'Montserrat',sans-serif;font-weight:500;font-size:18px;display:flex;align-items:center;justify-content:center}

/* welcome */
.welcome-photo{left:111px;top:746px;width:463px;height:510px;background:linear-gradient(135deg,#d8d8d8,#f4f4f2 40%,#c9b15a 75%,#8a8a8a);z-index:2}
.welcome-title{left:639px;top:772px;font-family:'Montserrat',sans-serif;font-weight:500;font-size:36px;color:#111}
.welcome-text{left:639px;top:836px;width:430px;font-size:16px;line-height:27px;color:#666}
.welcome-text p+p{margin-top:26px}
.btn-dark{background:#1a1a1a;color:var(--white);font-family:'Montserrat',sans-serif;font-weight:500;display:flex;align-items:center;justify-content:center}
.welcome-btn{left:639px;top:1053px;width:148px;height:53px;font-size:16px}

/* services */
.services{left:0;top:1185px;width:1200px;height:450px;background:var(--orange)}
.section-title{width:1200px;left:0;text-align:center;font-family:'Montserrat',sans-serif;font-weight:500;font-size:36px}
.services .section-title{top:132px;color:var(--white)}
.service{width:300px;text-align:center;color:var(--white);font-family:'Montserrat',sans-serif;font-weight:500;font-size:21px}
.service svg{display:block;margin:0 auto 28px}

/* products */
.products-title{top:1702px;color:#111}
.tile{overflow:hidden}
.tile .shade{position:absolute;left:0;right:0;bottom:0;height:45%;background:linear-gradient(transparent,rgba(0,0,0,.6))}
.tile .label{position:absolute;left:0;right:0;bottom:28px;text-align:center;font-family:'Montserrat',sans-serif;font-weight:600;font-size:21px;color:var(--white)}

/* testimonials */
.testimonials{left:0;top:2868px;width:1200px;height:597px;background:var(--light)}
.testimonials .section-title{top:68px;color:#111}
.avatar{left:525px;top:146px;width:150px;height:150px;border-radius:50%;background:#a7a7a7;overflow:hidden}
.quote{left:200px;top:318px;width:800px;text-align:center;font-style:italic;font-size:21px;line-height:32px;color:#555}
.quote-name{left:0;top:432px;width:1200px;text-align:center;font-family:'Montserrat',sans-serif;font-weight:500;font-size:20px;color:#222}

/* enquiry */
.enquiry-photo{left:667px;top:3393px;width:422px;height:510px;background:linear-gradient(150deg,#c9852a,#efe6d6 35%,#ffffff 55%,#c4cbd4 75%,#b9621e)}
.enquiry-title{left:108px;top:3532px;font-family:'Montserrat',sans-serif;font-weight:500;font-size:36px;color:#111}
.field{border:1px solid #cfcfcf;background:var(--white);font-size:16px;color:#888;padding:12px 14px}
.send-btn{left:111px;top:3862px;width:117px;height:53px;font-size:17px}

/* footer */
.footer{left:0;top:3996px;width:1200px;height:422px;background:var(--footer);color:#e8e8e8}
.footer-logo{left:111px;top:90px;display:flex;align-items:center;gap:14px;font-family:'Montserrat',sans-serif;font-weight:700;font-size:52px;color:var(--white)}
.footer-logo .dot{width:36px;height:36px;border-radius:50%;background:var(--white)}
.footer-vat{left:111px;top:252px;font-family:'Montserrat',sans-serif;font-weight:500;font-size:19px;color:var(--white)}
.footer-head{font-family:'Montserrat',sans-serif;font-weight:500;font-size:20px;color:var(--white)}
.footer-links{left:471px;top:118px;font-size:16px;line-height:31px}
.contact-line{font-size:16px;line-height:24px;display:flex;gap:14px}
.footer-rule{left:111px;top:322px;width:978px;height:1px;background:#555}
.copyright{left:111px;top:357px;font-size:16px}
.social{top:343px;width:48px;height:48px;border:2px solid #ddd;border-radius:50%}
</style>
</head>
<body>

<header>
  <div class="abs site-logo"><span class="dot"></span>Kelvaro</div>
  <div class="abs topbar">
    <svg width="14" height="14" viewBox="0 0 24 24"><path fill="#e98c41" d="M6.6 10.8a15 15 0 0 0 6.6 6.6l2.2-2.2c.3-.3.7-.4 1-.2 1.1.4 2.3.6 3.6.6.6 0 1 .4 1 1V20c0 .6-.4 1-1 1A17 17 0 0 1 3 4c0-.6.4-1 1-1h3.5c.6 0 1 .4 1 1 0 1.3.2 2.5.6 3.6.1.3 0 .7-.2 1z"/></svg>
    <span>+41 71 555 02 18</span><span>|</span>
    <svg width="16" height="13" viewBox="0 0 24 18"><rect width="24" height="18" rx="2" fill="#e98c41"/><path d="M1 2l11 8 11-8" stroke="#fff" stroke-width="2" fill="none"/></svg>
    <span>info@kelvaro.ch</span>
    <span class="lang">Eng ⌄</span>
  </div>
  <nav class="abs main-nav">
    <span class="active" style="left:0">HOME</span>
    <span style="left:89px">ABOUT US</span>
    <span style="left:216px">SERVICES</span>
    <span style="left:336px">PRODUCTS</span>
    <span style="left:470px">CONTACT</span>
    <svg style="position:absolute;left:588px;top:3px" width="16" height="16" viewBox="0 0 24 24"><circle cx="10" cy="10" r="7" stroke="#222" stroke-width="3" fill="none"/><path d="M15 15l7 7" stroke="#222" stroke-width="3"/></svg>
  </nav>
</header>

<section>
  <div class="abs hero" role="img" aria-label="Woman wearing a crimson cotton headscarf on a city street"></div>
  <h1 class="abs hero-title">KELVARO</h1>
  <p class="abs hero-sub">Specialized in production and trading of<br>high-quality cotton fabrics/products</p>
  <div class="abs btn-light">ORDER NOW!</div>
</section>

<section>
  <div class="abs welcome-photo" role="img" aria-label="White thread spools on a textile machine"></div>
  <h2 class="abs welcome-title">WELCOME TO KELVARO</h2>
  <div class="abs welcome-text">
    <p>Kelvaro GmbH is a textile company that is specialized in production and trading of high-quality cotton fabrics/ products.</p>
    <p>Nemo enim ipsam voluptatem quia voluptas sit arnatur aut odit aut fugit, sed quia consequuntur magni dolore silos qui ratione voluptatem sequi nesc.</p>
  </div>
  <div class="abs btn-dark welcome-btn">READ MORE</div>
</section>

<section class="abs services">
  <h2 class="abs section-title">WHAT WE DO</h2>
  <div class="abs service" style="left:69px;top:230px">
    <svg width="110" height="110" viewBox="0 0 110 110" fill="none" stroke="#fff" stroke-width="3"><path d="M55 50L10 70l45 20 45-20z"/><path d="M10 80l45 20 45-20"/><path d="M10 90l45 20 45-20" transform="translate(0,-8)"/><path d="M48 8h14v40l-7 10-7-10z"/></svg>
    Design and Develop
  </div>
  <div class="abs service" style="left:347px;top:230px">
    <svg width="110" height="110" viewBox="0 0 110 110" fill="none" stroke="#fff" stroke-width="3"><circle cx="55" cy="60" r="44"/><circle cx="55" cy="60" r="36"/><rect x="45" y="6" width="20" height="10" rx="3"/><path d="M90 14L60 72"/><rect x="78" y="70" width="20" height="34"/><path d="M38 45l10 10M48 45L38 55M38 62l10 10M48 62L38 72"/></svg>
    Special Weaving
  </div>
  <div class="abs service" style="left:556px;top:230px">
    <svg width="110" height="110" viewBox="0 0 110 110" fill="none" stroke="#fff" stroke-width="3"><path d="M30 14h66L60 100H20z"/><path d="M24 14v86" stroke-dasharray="8 6"/><path d="M64 14v40" stroke-dasharray="8 6"/></svg>
    Shear
  </div>
  <div class="abs service" style="left:813px;top:230px">
    <svg width="120" height="110" viewBox="0 0 120 110" fill="none" stroke="#fff" stroke-width="3"><path d="M60 8l50 20-50 20-50-20z"/><path d="M10 28v50l50 24 50-24V28"/><path d="M60 48v54"/><rect x="24" y="56" width="24" height="24"/><rect x="72" y="56" width="24" height="24"/></svg>
    Logo printing &amp; Packing
  </div>
</section>

<section>
  <h2 class="abs section-title products-title">OUR PRODUCTS</h2>
  <div class="abs tile" style="left:111px;top:1785px;width:482px;height:330px;background:linear-gradient(160deg,#8c8c8c,#d8d8d8 45%,#b0b0b0)" role="img" aria-label="Folded white Swiss Ghutra fabric"><div class="shade"></div><div class="label">Swiss Ghutra</div></div>
  <div class="abs tile" style="left:607px;top:1785px;width:482px;height:330px;background:linear-gradient(160deg,#3a2a2a,#c8303e 30%,#f2e8e8 55%,#d13a45 80%)" role="img" aria-label="Red and white Shemagh fabric"><div class="shade"></div><div class="label">Shemagh (=Yashmagh)</div></div>
  <div class="abs tile" style="left:111px;top:2131px;width:316px;height:308px;background:linear-gradient(160deg,#e8e6e2,#cdb9a8 40%,#f3f1ee 70%)" role="img" aria-label="Young men in white Desdasha robes"><div class="shade"></div><div class="label">Desdasha’s</div></div>
  <div class="abs tile" style="left:442px;top:2131px;width:316px;height:308px;background:linear-gradient(160deg,#b7c9d8,#c4863c 35%,#5a3422 60%,#a7bccc)" role="img" aria-label="Woman in a colourful head wrap"><div class="shade"></div><div class="label">Emmas and Shawls</div></div>
  <div class="abs tile" style="left:773px;top:2131px;width:316px;height:308px;background:linear-gradient(160deg,#c8d0dc,#eef0f4 45%,#aeb8c8)" role="img" aria-label="White brocade damask fabric"><div class="shade"></div><div class="label">Brocade/Damask</div></div>
  <div class="abs tile" style="left:111px;top:2455px;width:482px;height:331px;background:linear-gradient(100deg,#b8b3aa,#ece9e2 40%,#d8d4cc 70%,#f2f0ec)" role="img" aria-label="Draped white Atiku fabric"><div class="shade"></div><div class="label">Atiku</div></div>
  <div class="abs tile" style="left:607px;top:2455px;width:482px;height:331px;background:radial-gradient(ellipse at 50% 55%,#6fb3c7 0%,#8cc3d2 25%,#f3f3f3 45%)" role="img" aria-label="Mannequin draped in blue checked voile"><div class="shade"></div><div class="label">Teminor Voile</div></div>
</section>

<section class="abs testimonials">
  <h2 class="abs section-title">CLIENT TESTIMONIALS</h2>
  <div class="abs avatar">
    <svg width="150" height="150" viewBox="0 0 150 150"><circle cx="75" cy="58" r="30" fill="#fff"/><ellipse cx="75" cy="140" rx="52" ry="44" fill="#fff"/></svg>
  </div>
  <p class="abs quote">“ Sed ut perspiciatis unde omnis iste natus error sit voluptatem acsantium dol oremque laudantium, totam rem aperiam, eaque ipsa quae ab illo invent ore ver itatis et quasi architecto beatae vitae dicta sunt explicabo.“</p>
  <div class="abs quote-name">- LUCAS</div>
  <svg class="abs" style="left:110px;top:352px" width="20" height="34" viewBox="0 0 20 34"><path d="M17 2L3 17l14 15" stroke="#999" stroke-width="3" fill="none"/></svg>
  <svg class="abs" style="left:1068px;top:352px" width="20" height="34" viewBox="0 0 20 34"><path d="M3 2l14 15L3 32" stroke="#999" stroke-width="3" fill="none"/></svg>
</section>

<section>
  <div class="abs enquiry-photo" role="img" aria-label="Close-up of threads on a weaving loom"></div>
  <h2 class="abs enquiry-title">ENQUIRY FORM</h2>
  <div class="abs field" style="left:111px;top:3605px;width:256px;height:48px">Name:</div>
  <div class="abs field" style="left:377px;top:3605px;width:256px;height:48px">Email:</div>
  <div class="abs field" style="left:111px;top:3667px;width:256px;height:48px">Phone:</div>
  <div class="abs field" style="left:377px;top:3667px;width:256px;height:48px">Address:</div>
  <div class="abs field" style="left:111px;top:3729px;width:522px;height:106px">Message:</div>
  <div class="abs btn-dark send-btn">SEND</div>
</section>

<footer class="abs footer">
  <div class="abs footer-logo"><span class="dot"></span>Kelvaro</div>
  <div class="abs footer-vat">CHE-218.904.337 MWST</div>
  <div class="abs footer-head" style="left:471px;top:68px">Quick Links</div>
  <div class="abs footer-links">Home<br>About us<br>Services<br>Products<br>Contact</div>
  <div class="abs footer-head" style="left:703px;top:68px">Contact Information</div>
  <div class="abs contact-line" style="left:703px;top:114px">
    <svg width="12" height="18" viewBox="0 0 12 18"><path d="M6 0a6 6 0 0 0-6 6c0 5 6 12 6 12s6-7 6-12a6 6 0 0 0-6-6z" fill="#fff"/><circle cx="6" cy="6" r="2.2" fill="#262626"/></svg>
    <span>Talackerweg 14<br>CH – 9043 Lindbühl<br>&nbsp;Switzerland</span>
  </div>
  <div class="abs contact-line" style="left:703px;top:211px">
    <svg width="16" height="16" viewBox="0 0 24 24"><path fill="#fff" d="M6.6 10.8a15 15 0 0 0 6.6 6.6l2.2-2.2c.3-.3.7-.4 1-.2 1.1.4 2.3.6 3.6.6.6 0 1 .4 1 1V20c0 .6-.4 1-1 1A17 17 0 0 1 3 4c0-.6.4-1 1-1h3.5c.6 0 1 .4 1 1 0 1.3.2 2.5.6 3.6.1.3 0 .7-.2 1z"/></svg>
    <span>+41 71 555 02 18</span>
  </div>
  <div class="abs contact-line" style="left:703px;top:259px">
    <svg width="18" height="14" viewBox="0 0 24 18"><rect width="24" height="18" rx="2" fill="#fff"/><path d="M1 2l11 8 11-8" stroke="#262626" stroke-width="2" fill="none"/></svg>
    <span>info@kelvaro.ch</span>
  </div>
  <div class="abs footer-rule"></div>
  <div class="abs copyright">Copyright © 2021, Kelvaro. All rights reserved.</div>
  <div class="abs social" style="left:929px"></div>
  <div class="abs social" style="left:986px"></div>
  <div class="abs social" style="left:1041px"></div>
</footer>

</body>
</html>
```